TWS Business Card Design

As a full service media and advocacy firm, we lean on years of experience in political and corporate consulting, grassroots campaigning, media placement, and video production to deliver unparalleled results. Recently we have moved into digital media and now provide this service for our clients.

I will add our two company logos to be used on the business cards. The longer logo with "sky reach studio" is our primary logo. Our secondary logo is more square one with "sky reach" and 'digital.media.campaigns" on it. We are looking for clean and modern looking business cards fitting for a digital firm.

I will also add our logos that go well with dark backgrounds.

Industry/Entity Type

Political

Contact Information for Business Card

Denton Pratchard, Director of Campaigns and Digital, 571-482-7165, denton@skyreachstudioco.com, @SkyReachStudioCo, @DentonPratchard, Facebook.com/SkyReachStudioCo

```html
<!DOCTYPE html>
<html lang="en">
<head>
<meta charset="utf-8">
<title>TWS Business Card</title>
<link rel="stylesheet" href="https://fonts.googleapis.com/css2?family=Montserrat:ital,wght@0,400;0,600;0,700;1,400&display=swap">
<style>
  :root {
    --backdrop: #3a3330;
    --card: #ffffff;
    --navy: #1f2d8a;
    --sky: #1e90dc;
    --ink: #2a2a2a;
  }
  html, body {
    margin: 0;
    width: 1200px;
    height: 768px;
    overflow: hidden;
    background: var(--backdrop);
    font-family: "Montserrat", sans-serif;
  }
  .stage {
    position: relative;
    width: 1200px;
    height: 768px;
  }
  .card {
    position: absolute;
    top: 234px;
    width: 520px;
    height: 300px;
    background: var(--card);
    box-shadow: 0 6px 18px rgba(0,0,0,0.35);
    overflow: hidden;
  }
  .card-front { left: 50px; }
  .card-back { left: 630px; }

  .front-brand {
    position: absolute;
    inset: 0;
    display: flex;
    align-items: center;
    justify-content: center;
    gap: 14px;
  }
  .front-brand .brand-dot {
    width: 22px;
    height: 22px;
    border-radius: 50%;
    background: var(--sky);
  }
  .front-brand .brand-name {
    font-size: 40px;
    font-weight: 600;
    color: var(--sky);
    text-transform: uppercase;
    letter-spacing: 1px;
  }

  .holder {
    position: absolute;
    left: 38px;
    top: 34px;
  }
  .holder-name {
    margin: 0;
    font-size: 17px;
    font-weight: 700;
    color: var(--navy);
  }
  .holder-title {
    margin: 3px 0 0;
    font-size: 9.5px;
    font-style: italic;
    color: var(--ink);
  }

  .contacts {
    position: absolute;
    left: 38px;
    top: 132px;
    margin: 0;
    padding: 0;
    list-style: none;
    font-size: 12.5px;
    color: var(--ink);
  }
  .contacts li {
    display: flex;
    align-items: center;
    gap: 8px;
    height: 19px;
  }
  .contacts svg {
    width: 11px;
    height: 11px;
    flex: none;
    fill: var(--navy);
  }
  .contacts .accent { color: var(--sky); }

  .back-brand {
    position: absolute;
    right: 36px;
    top: 112px;
    display: flex;
    align-items: center;
    gap: 10px;
  }
  .back-brand .brand-dot {
    width: 16px;
    height: 16px;
    border-radius: 50%;
    background: var(--navy);
  }
  .back-brand .brand-name {
    font-size: 34px;
    font-weight: 700;
    color: var(--navy);
    text-transform: uppercase;
  }

  .edge-bands {
    position: absolute;
    left: 0;
    bottom: 0;
    width: 520px;
    height: 40px;
  }
</style>
</head>
<body>
<main class="stage">
  <section class="card card-front" aria-label="Card front">
    <div class="front-brand">
      <span class="brand-dot"></span>
      <span class="brand-name">Sky Reach Studio</span>
    </div>
  </section>

  <section class="card card-back" aria-label="Card back">
    <div class="holder">
      <h1 class="holder-name">Denton Pratchard</h1>
      <p class="holder-title">Director of Campaigns &amp; Digital</p>
    </div>

    <ul class="contacts">
      <li>
        <svg viewBox="0 0 12 12" aria-hidden="true"><path d="M2.5 1 L4.5 1 L5.3 3.4 L4 4.4 Q5 6.8 7.6 8 L8.6 6.7 L11 7.5 L11 9.5 Q11 11 9.5 11 Q1 10.5 1 2.5 Q1 1 2.5 1 Z"/></svg>
        <span>571-482-7165</span>
      </li>
      <li>
        <svg viewBox="0 0 12 12" aria-hidden="true"><rect x="1" y="1" width="10" height="10" rx="1.5"/></svg>
        <span>/SkyReachStudioCo</span>
      </li>
      <li>
        <svg viewBox="0 0 12 12" aria-hidden="true"><path d="M1 2.5 H11 V9.5 H1 Z M1.6 3 L6 6.6 L10.4 3" stroke="#fff" stroke-width="0.9"/></svg>
        <span>denton@<span class="accent">skyreachstudioco.com</span></span>
      </li>
      <li>
        <svg viewBox="0 0 12 12" aria-hidden="true"><path d="M1 2.5 H11 V9.5 H1 Z M1.6 3 L6 6.6 L10.4 3" stroke="#fff" stroke-width="0.9"/></svg>
        <span>@SkyReachStudioCo, @DentonPratchard</span>
      </li>
    </ul>

    <div class="back-brand">
      <span class="brand-dot"></span>
      <span class="brand-name">Sky Reach</span>
    </div>

    <svg class="edge-bands" viewBox="0 0 520 40" preserveAspectRatio="none" aria-hidden="true">
      <polygon points="0,12 300,24 318,40 0,40" fill="var(--navy)"/>
      <polygon points="300,24 520,33 520,40 318,40" fill="var(--sky)"/>
    </svg>
  </section>
</main>
</body>
</html>
```